Young Accounting firm needing a captivating business card

We need a business card design that forces the person to look at the card because its either gold foil, plastic, or lettering pop up etc. We already have a logo with a specific gold color and we need to make it pop. We are an accounting firm. I need the words" accounting, payroll, licenses, audits, taxes" somewhere on the business card so as to describe what we do- preferably on the side where the logo is at.

Industry/Entity Type

Accounting

Contact Information for Business Card

Address 48276 9th Ave S Ste 305, Federal Way, WA 98117
Business Phone (360)418-2096
Fax (360)418-2157
Office Cell Phone (360)586-7319

Font styles to use
Serif

Colors
85abd2

Requirements
Must have
• It should state
• "Accounting" "Taxes" "Audits" "Licenses" "Payroll"
Nice to have
• Matte with gold foil, different textures, With Either a textured ivory background or gray blue slate background
Should not have
• colorful colors

```html
<!DOCTYPE html>
<html lang="en">
<head>
<meta charset="utf-8">
<title>Kestrel Ledger – Business Card</title>
<link href="https://fonts.googleapis.com/css2?family=EB+Garamond:wght@400;500&display=swap" rel="stylesheet">
<style>
  :root {
    --backdrop: #3b3029;
    --card: #262626;
    --card-edge: #1a1a1c;
    --gold: #c9a227;
    --gold-soft: #b8952a;
    --ink-muted: #9a9a9a;
  }
  * { margin: 0; padding: 0; box-sizing: border-box; }
  html, body { width: 1200px; height: 715px; overflow: hidden; }
  body {
    background: var(--backdrop);
    font-family: "EB Garamond", Georgia, serif;
    position: relative;
  }
  .card {
    position: absolute;
    width: 500px;
    height: 286px;
    background: var(--card);
    box-shadow: 0 3px 0 var(--card-edge), 0 10px 24px rgba(0,0,0,.45);
    overflow: hidden;
  }
  .card--back { left: 60px; top: 215px; }
  .card--front { left: 640px; top: 215px; }

  /* back */
  .back-brand {
    position: absolute; left: 0; right: 0; top: 92px;
    display: flex; align-items: center; justify-content: center; gap: 14px;
  }
  .brand-mark { width: 30px; height: 30px; background: var(--gold); }
  .back-brand .brand-name {
    font-size: 40px; font-weight: 500; color: var(--gold); letter-spacing: .5px;
  }
  .back-web {
    position: absolute; left: 0; right: 0; bottom: 40px; text-align: center;
    font-size: 12px; letter-spacing: 2.5px; color: var(--gold-soft);
  }

  /* front */
  .front-brand {
    position: absolute; right: 56px; top: 40px; text-align: center;
  }
  .front-brand .brand-row { display: flex; align-items: center; gap: 10px; justify-content: center; }
  .front-brand .brand-mark { width: 20px; height: 20px; }
  .front-brand .brand-name { font-size: 30px; font-weight: 500; color: var(--gold); line-height: 1; }
  .brand-rule { height: 1.5px; background: var(--gold); margin-top: 5px; }
  .services { font-size: 8px; color: var(--gold-soft); margin-top: 3px; letter-spacing: .3px; }

  .divider {
    position: absolute; left: 150px; right: 70px; top: 132px;
    height: 2px; background: var(--gold);
  }
  .contact-list { position: absolute; left: 34px; top: 46px; list-style: none; }
  .contact-list li {
    display: flex; align-items: center; gap: 12px;
    font-size: 12px; color: var(--ink-muted); height: 20px;
  }
  .contact-list svg { width: 10px; height: 10px; fill: var(--gold); flex: none; }

  .person { position: absolute; right: 56px; top: 146px; }
  .person-name { font-size: 16px; color: var(--gold); }
  .person-title { font-size: 13px; color: var(--ink-muted); }

  .address {
    position: absolute; right: 56px; bottom: 30px;
    font-size: 14px; color: var(--gold); line-height: 1.3;
  }
</style>
</head>
<body>

<section class="card card--back">
  <div class="back-brand">
    <span class="brand-mark"></span>
    <span class="brand-name">Kestrel Ledger</span>
  </div>
  <p class="back-web">www.kestrelledger.com</p>
</section>

<section class="card card--front">
  <div class="front-brand">
    <div class="brand-row">
      <span class="brand-mark"></span>
      <span class="brand-name">Kestrel Ledger</span>
    </div>
    <div class="brand-rule"></div>
    <p class="services">Accounting, Payroll, Licenses, Audits, Taxes</p>
  </div>

  <ul class="contact-list">
    <li><svg viewBox="0 0 10 10"><path d="M1 3h8v1.5H7V3.8H3v.7H1z M2 5h6l1 4H1z"/></svg>(360)418-2096</li>
    <li><svg viewBox="0 0 10 10"><path d="M2.5 1h5v3h-5z M1 4.5h8V8H7.5v1.5h-5V8H1z"/></svg>(360)418-2157</li>
    <li><svg viewBox="0 0 10 10"><path d="M2 1l2 .5.5 2-1 1a5 5 0 0 0 2 2l1-1 2 .5L9 8c-3 1.5-8-3.5-7-7z"/></svg>(360)586-7319</li>
    <li><svg viewBox="0 0 10 10"><path d="M1 2.5h8v5H1z M1.5 3l3.5 2.5L8.5 3" stroke="#262626" stroke-width=".7"/></svg>maren.holt@kestrelledger.com</li>
  </ul>

  <div class="divider"></div>

  <div class="person">
    <p class="person-name">Maren Holt</p>
    <p class="person-title">Practise Manager</p>
  </div>

  <address class="address" style="font-style:normal">
    48276 9th Ave S Ste 305<br>
    Federal Way, WA 98117
  </address>
</section>

</body>
</html>
```